Marlene Business Card

My wife is going to start her own business with renting holiday appartments to tourists. She needs a design for a new business card... and a new web site.
Look at Roomvesta "Ruhezeit am Birkenteich"

Target Market(s)

Give business card to prospects at any situation

Contact Information for Business Card

not sure what this means

Font styles to use
Script

Colors
fec41a
fee18a

Requirements
Must have
• My wife's handwriting is difficult to read:
Entspannen - Loslassen - Auftanken
Marlene & der Birkenteich
Urlaub an einem besonderen Ort
Marlene Brökel
Gartenpfad 7
17489 Alt Medow
info@marlene-broekel.de
www.birkenteich.net
Nice to have
• Beige background
Font like handwriting

```html
<!DOCTYPE html>
<html lang="de">
<head>
<meta charset="utf-8">
<title>Marlene & der Birkenteich – Visitenkarte</title>
<link rel="stylesheet" href="https://fonts.googleapis.com/css2?family=Dancing+Script:wght@500;600&family=Crimson+Text:wght@400&display=swap">
<style>
  :root {
    --sun: #fec41a;
    --sun-light: #fce97a;
    --earth: #9a6b2f;
    --paper: #ffffff;
    --page: #ffffff;
    --shadow: rgba(0, 0, 0, 0.28);
  }
  * { margin: 0; padding: 0; box-sizing: border-box; }
  html, body {
    width: 1200px;
    height: 1000px;
    overflow: hidden;
    background: var(--page);
  }
  .canvas {
    position: relative;
    width: 1200px;
    height: 1000px;
  }
  .card {
    position: absolute;
    left: 245px;
    width: 711px;
    height: 407px;
    background: var(--paper);
    box-shadow: 2px 4px 7px var(--shadow);
    overflow: hidden;
  }
  .card--front { top: 70px; }
  .card--back { top: 523px; }

  .script {
    font-family: "Dancing Script", cursive;
    font-weight: 500;
    color: var(--sun);
    white-space: nowrap;
  }
  .serif {
    font-family: "Crimson Text", serif;
    color: var(--earth);
    white-space: nowrap;
  }

  /* Front */
  .front__brand {
    position: absolute;
    right: 52px;
    top: 54px;
    font-size: 39px;
    line-height: 1;
  }
  .front__name {
    position: absolute;
    left: 50px;
    top: 205px;
    font-size: 45px;
    font-weight: 500;
    line-height: 1;
  }
  .front__rule {
    position: absolute;
    left: 51px;
    right: 51px;
    top: 276px;
    height: 3px;
    background: var(--sun);
  }
  .front__contact {
    position: absolute;
    top: 308px;
    font-size: 18.5px;
    line-height: 24px;
    font-style: normal;
  }
  .front__contact--address { left: 51px; }
  .front__contact--online { right: 51px; text-align: right; }

  /* Back */
  .back__frame {
    position: absolute;
    inset: 0;
  }
  .back__values {
    position: absolute;
    left: 0;
    right: 0;
    top: 52px;
    text-align: center;
    font-size: 28px;
    line-height: 1;
    letter-spacing: 0.5px;
  }
  .back__brand {
    position: absolute;
    left: 0;
    right: 0;
    top: 170px;
    text-align: center;
    font-size: 62px;
    font-weight: 500;
    line-height: 1;
  }
  .back__slogan {
    position: absolute;
    left: 0;
    right: 0;
    top: 254px;
    text-align: center;
    font-size: 30px;
    line-height: 1;
    color: var(--earth);
  }
  .back__rule {
    position: absolute;
    top: 268px;
    width: 100px;
    height: 4px;
    background: var(--sun);
  }
  .back__rule--left { left: 51px; }
  .back__rule--right { right: 51px; }
</style>
</head>
<body>
<main class="canvas">

  <section class="card card--front" aria-label="Vorderseite">
    <p class="front__brand script">Marlene &amp; der Birkenteich</p>
    <h1 class="front__name script">Marlene Brökel</h1>
    <div class="front__rule"></div>
    <address class="front__contact front__contact--address serif">
      Gartenpfad 7<br>17489 Alt Medow
    </address>
    <p class="front__contact front__contact--online serif">
      info@marlene-broekel.de<br>www.birkenteich.net
    </p>
  </section>

  <section class="card card--back" aria-label="Rückseite">
    <svg class="back__frame" width="711" height="407" viewBox="0 0 711 407" aria-hidden="true">
      <polygon points="0,0 711,0 686,25 25,25" fill="var(--sun-light)"/>
      <polygon points="0,407 711,407 686,382 25,382" fill="var(--sun-light)"/>
      <polygon points="0,0 25,25 25,382 0,407" fill="var(--sun)"/>
      <polygon points="711,0 686,25 686,382 711,407" fill="var(--sun)"/>
    </svg>
    <p class="back__values serif">Entspannen • Loslassen • Auftanken</p>
    <h2 class="back__brand script">Marlene &amp; der Birkenteich</h2>
    <div class="back__rule back__rule--left"></div>
    <p class="back__slogan script">Urlaub an einem besonderen Ort</p>
    <div class="back__rule back__rule--right"></div>
  </section>

</main>
</body>
</html>
```